WooCommerce Web Design for SEO Agency

Looking for a clean and fast WooCommerce design

Selling 5 different products each with maybe 3-4 variants

Need imagery - featured images, basic logo etc

I will supply all content and most is ready to go (or can be in a few days)

You will need to design and build the site including some basic WooCommerce configuration - PayPal, checkout forms etc

Target Market(s)

SEO, Internet marketers

Coding

Coded - Design and coding required

Number of Pages Required

3 page

Font styles to use
Sans Serif

Requirements
Must have
• WooCommerce and WP integration

```html
<!DOCTYPE html>
<html lang="en">
<head>
<meta charset="utf-8">
<title>RankHarbor – Boost your web traffic</title>
<link href="https://fonts.googleapis.com/css2?family=Ubuntu:wght@400;500;700&family=Lato:wght@400;700&display=swap" rel="stylesheet">
<style>
:root{
  --blue:#1d6fe0;
  --blue-deep:#0d3fc4;
  --blue-light:#3a8ef0;
  --purple:#7a3fd4;
  --purple-soft:#8f5be0;
  --ink:#1c1c28;
  --text:#6d6f7b;
  --accent:#4a3fcf;
  --line:#dfe3ee;
  --white:#ffffff;
  --pale:#f3f6fc;
  --sky:#8fd0ff;
}
*{box-sizing:border-box;margin:0;padding:0}
html,body{width:1200px;height:5296px;overflow:hidden}
body{position:relative;background:var(--white);font-family:"Lato",sans-serif;color:var(--text)}
.abs{position:absolute}
h1,h2,h3,h4{font-family:"Ubuntu",sans-serif;color:var(--ink);font-weight:500}
.ph{position:absolute;overflow:hidden}
.btn{position:absolute;display:flex;align-items:center;justify-content:center;gap:10px;font-size:12px;border-radius:5px;font-family:"Lato",sans-serif}
.btn-outline{border:1px solid var(--line);background:var(--white);color:var(--accent);box-shadow:0 4px 12px rgba(30,60,140,.08)}
.btn-dark{background:var(--accent);color:var(--white)}
.eyebrow{position:absolute;font-size:11px;letter-spacing:.5px;color:var(--accent);text-transform:uppercase}
.para{position:absolute;font-size:11.5px;line-height:16px;color:var(--text)}
/* header */
.nav{position:absolute;top:28px;left:0;width:1200px;height:20px}
.brand{position:absolute;font-family:"Ubuntu",sans-serif;font-weight:500;font-size:22px;color:var(--white);white-space:nowrap}
.menu{position:absolute;top:3px;left:410px;display:flex;gap:28px;font-size:12.5px;color:var(--white)}
.hero-title{position:absolute;left:199px;top:192px;font-size:56px;line-height:64px;color:var(--white);font-weight:500}
/* category cards */
.cat{position:absolute;width:176px;height:218px;border-radius:6px;padding:28px 18px 0 38px;color:var(--white);font-family:"Lato",sans-serif;font-size:17px;line-height:22px;box-shadow:0 14px 30px rgba(60,40,160,.25)}
.cat.purple{background:linear-gradient(160deg,var(--purple-soft),var(--purple))}
.cat.blue{background:linear-gradient(160deg,var(--blue-light),var(--blue))}
.cat .art{position:absolute;left:42px;bottom:36px;width:72px;height:62px;border-radius:4px;background:linear-gradient(135deg,#eaf1ff,#a9c4f5)}
/* products */
.prod{position:absolute;width:226px;height:255px;background:var(--white);border-radius:6px;box-shadow:0 10px 30px rgba(40,70,150,.14);text-align:center;overflow:hidden}
.prod::after{content:"";position:absolute;right:-40px;bottom:-40px;width:150px;height:150px;border-radius:50%;background:var(--pale)}
.prod .ic{position:relative;z-index:1;width:50px;height:50px;border-radius:50%;background:var(--blue);margin:34px auto 18px;display:flex;align-items:center;justify-content:center}
.prod .ic span{width:22px;height:22px;border:2px solid var(--white);border-radius:4px}
.prod h4{position:relative;z-index:1;font-family:"Lato",sans-serif;font-size:12px;line-height:16px;color:var(--ink);font-weight:700}
.prod .price{position:relative;z-index:1;font-size:13px;color:var(--ink);margin-top:10px}
.prod .add{position:relative;z-index:1;display:inline-block;margin-top:18px;background:var(--accent);color:var(--white);font-size:12px;padding:8px 14px;border-radius:4px}
.overlay-title{position:absolute;color:var(--white);font-family:"Ubuntu",sans-serif;font-weight:500;font-size:44px;line-height:56px}
/* skills */
.skill{position:absolute;left:117px;width:432px}
.skill .lbl{display:flex;justify-content:space-between;font-size:12.5px;color:var(--accent)}
.skill .track{margin-top:8px;height:3px;background:var(--line)}
.skill .fill{height:3px;background:var(--accent)}
/* accordion */
.acc{position:absolute;left:639px;width:444px;border:1px solid var(--line);border-radius:4px;background:var(--white);box-shadow:0 4px 12px rgba(40,70,150,.08);font-size:12.5px;color:var(--accent);padding:8px 14px}
.acc .dot{position:absolute;right:12px;top:6px;width:20px;height:20px;border-radius:50%;background:var(--blue-light)}
/* case studies */
.case{position:absolute;top:3781px;height:202px;width:308px}
.case b{position:absolute;left:20px;top:110px;color:var(--white);font-family:"Ubuntu",sans-serif;font-size:21px;font-weight:500;white-space:nowrap}
.case small{position:absolute;left:20px;top:138px;color:var(--white);font-size:11px}
/* blog */
.post{position:absolute;top:4285px;width:310px}
.post .img{height:202px}
.post .date,.post h3,.post .more{padding-left:6px}
.post .date{font-size:11.5px;color:var(--text);margin-top:26px}
.post h3{font-size:19px;line-height:25px;margin-top:12px;color:var(--ink);width:270px}
.post .more{font-size:11px;color:var(--accent);margin-top:12px;font-weight:700}
/* footer */
.fcol{position:absolute;top:4955px;width:300px;text-align:center;color:var(--white)}
.fcol svg{display:block;margin:0 auto 14px}
.fcol p{font-size:15px}
.fcol span{display:block;font-size:14px;color:var(--sky);margin-top:8px}
.fmenu{position:absolute;top:5120px;left:0;width:1200px;display:flex;justify-content:center;gap:26px;font-size:12px;color:var(--white)}
.social{position:absolute;top:5178px;width:26px;height:26px;border-radius:50%;background:var(--white)}
</style>
</head>
<body>

<svg class="abs" style="left:0;top:0" width="1200" height="640" viewBox="0 0 1200 640">
  <defs>
    <linearGradient id="heroGrad" x1="0" y1="0" x2="1" y2="1">
      <stop offset="0" stop-color="#2a86ee"/>
      <stop offset="1" stop-color="#1553d6"/>
    </linearGradient>
  </defs>
  <path d="M0 0H1200V470C1060 560 850 560 660 520C450 475 230 480 0 560Z" fill="url(#heroGrad)"/>
  <path d="M1090 0C1130 90 1200 120 1200 240V0Z" fill="#ffffff"/>
  <path d="M1200 260C1120 420 980 480 820 520C960 500 1100 450 1200 360Z" fill="#4da0f5" opacity=".5"/>
</svg>

<header class="nav">
  <div class="brand" style="left:120px;top:-5px">RankHarbor</div>
  <nav class="menu"><span>Home</span><span>About us</span><span>Shop</span><span>Category ▾</span><span>Project</span><span>Blog</span><span>Contact</span></nav>
  <div class="abs" style="left:886px;top:-8px;width:32px;height:32px;border-radius:4px;background:var(--white)"></div>
  <div class="abs" style="left:930px;top:-8px;width:104px;height:32px;border-radius:4px;background:var(--white);color:var(--blue);font-size:11px;display:flex;align-items:center;justify-content:center">Register Now</div>
  <div class="abs" style="left:1048px;top:-8px;width:32px;height:32px;border-radius:4px;background:var(--white)"></div>
</header>

<h1 class="hero-title">Boost your<br>web traffic</h1>
<p class="para" style="left:199px;top:327px;width:330px;color:#e3edff">Lorem ipsum dolor sit amet, consectetur adipiscing elit, sed do eiusmod tempor incididunt</p>
<div class="btn btn-dark" style="left:199px;top:386px;width:146px;height:35px;background:#2c3fc8">Shop Now</div>
<div class="btn btn-outline" style="left:362px;top:386px;width:146px;height:35px;border:none">Contact Now</div>
<div class="ph" role="img" aria-label="Illustration of a rocket launching from a computer screen with two people and plants" style="left:545px;top:110px;width:575px;height:365px;border-radius:30px;background:radial-gradient(circle at 50% 50%,#9fc8ff 0%,#5aa0f5 55%,rgba(60,140,240,0) 75%)"></div>

<div class="cat purple" style="left:117px;top:674px">Category Landing Page Content<div class="art" role="img" aria-label="Landing page icon"></div></div>
<div class="cat purple" style="left:306px;top:719px;padding-top:34px">Guest Blog Post Content<div class="art" role="img" aria-label="Blog post icon"></div></div>
<div class="cat blue" style="left:497px;top:826px;padding-top:52px">Dummy Landing Page Content<div class="art" role="img" aria-label="Landing page icon"></div></div>
<div class="cat blue" style="left:117px;top:917px;padding-top:66px">Digital PR<div class="art" role="img" aria-label="Digital PR icon"></div></div>
<div class="cat purple" style="left:306px;top:960px;padding-top:52px">Guest Post Outreach<div class="art" role="img" aria-label="Outreach icon"></div></div>

<h2 class="abs" style="left:715px;top:786px;font-size:30px">Shop By Category</h2>
<h3 class="abs" style="left:716px;top:835px;font-size:24px;color:var(--accent);font-weight:400">Provide Awsome Service</h3>
<p class="para" style="left:716px;top:878px;width:368px;text-align:justify">Sed ut perspiciatis unde omnis iste natus error sit voluptatem accusantium doloremque laudantium, totam rem aperiam, eaque ipsa quae ab illo inventore veritatis et quasi architecto beatae vitae dicta sunt explicabo. Nemo enim ipsam voluptatem quia voluptas sit aspernatur aut odit aut fugit, sed quia consequuntur magni</p>
<p class="abs" style="left:716px;top:975px;font-size:12px;color:var(--accent)">Read more →</p>
<div class="btn btn-outline" style="left:715px;top:1015px;width:120px;height:32px">Go to the shop</div>

<h2 class="abs" style="left:0;width:1200px;text-align:center;top:1272px;font-size:38px">Our Featured Products</h2>
<div class="prod" style="left:117px;top:1447px"><div class="ic"><span></span></div><h4>Category / Landing Page Content<br>500 Words</h4><p class="price">£149.00</p><span class="add">Add to basket</span></div>
<div class="prod" style="left:362px;top:1389px"><div class="ic"><span></span></div><h4>Category / Landing Page Content<br>1000 Words</h4><p class="price">£279.00</p><span class="add">Add to basket</span></div>
<div class="prod" style="left:608px;top:1447px"><div class="ic"><span></span></div><h4>Guest Blog Post Content<br>1000 words</h4><p class="price">£69.00</p><span class="add">Add to basket</span></div>
<div class="prod" style="left:853px;top:1389px"><div class="ic"><span></span></div><h4>Digital PR<br>Basic Campaign</h4><p class="price">£1,499.00</p><span class="add">Add to basket</span></div>
<div class="btn btn-dark" style="left:528px;top:1771px;width:144px;height:35px">Shop Now</div>

<div class="ph" role="img" aria-label="Photo of a team meeting around a table, seen from above" style="left:0;top:1915px;width:590px;height:374px;background:linear-gradient(135deg,#6a5d4e,#b9ad9c 60%,#d9dbe0)"></div>
<div class="overlay-title" style="left:127px;top:2052px">Be a leader<br>in your business</div>
<p class="eyebrow" style="left:639px;top:1986px">About us</p>
<h2 class="abs" style="left:639px;top:2008px;font-size:32px;line-height:37px">Grow Your Business<br>With Our SEO Agency</h2>
<p class="para" style="left:640px;top:2098px;width:444px;text-align:justify">Sed ut perspiciatis unde omnis iste natus error sit voluptatem accusantium doloremque laudantium, totam rem aperiam, eaque ipsa quae ab illo inventore veritatis et quasi architecto beatae vitae dicta sunt explicabo. Nemo enim ipsam voluptatem quia voluptas sit aspernatur aut odit aut fugit, sed quia consequunt.</p>
<div class="btn btn-outline" style="left:639px;top:2191px;width:124px;height:31px">Go to the shop</div>
<svg class="abs" style="left:1150px;top:2040px" width="50" height="195"><path d="M50 0C10 40 0 110 20 150C30 175 45 190 50 195Z" fill="#1d6fe0"/></svg>

<svg class="abs" style="left:0;top:2440px" width="45" height="175"><path d="M0 0C30 30 45 80 35 120C28 150 10 165 0 175Z" fill="#7a3fd4"/></svg>
<p class="eyebrow" style="left:117px;top:2523px">Experience</p>
<h2 class="abs" style="left:117px;top:2543px;font-size:32px">Pay for Qualified Traffic</h2>
<p class="para" style="left:117px;top:2600px;width:444px;text-align:justify">Sed ut perspiciatis unde omnis iste natus error sit voluptatem accusantium doloremque laudantium, totam rem aperiam, eaque ipsa quae ab illo inventore veritatis et quasi architecto beatae vitae dicta sunt explicabo. Nemo enim ipsam voluptatem quia voluptas sit aspernatur aut odit aut fugit, sed quia consequunt.</p>
<div class="skill" style="top:2694px"><div class="lbl"><span>SEO Analysis</span><span>90%</span></div><div class="track"><div class="fill" style="width:90%"></div></div></div>
<div class="skill" style="top:2738px"><div class="lbl"><span>SEO Audit</span><span>79%</span></div><div class="track"><div class="fill" style="width:79%"></div></div></div>
<div class="skill" style="top:2788px"><div class="lbl"><span>Optimization</span><span>95%</span></div><div class="track"><div class="fill" style="width:95%"></div></div></div>
<div class="btn btn-outline" style="left:117px;top:2881px;width:122px;height:31px">Get In Touch</div>
<div class="ph" role="img" aria-label="Photo of a smiling woman with curly hair and glasses in an office" style="left:610px;top:2431px;width:590px;height:553px;background:linear-gradient(160deg,#7a6150,#a88a70 45%,#5a4638)"></div>
<div class="overlay-title" style="left:727px;top:2652px">Expand Your<br>Digital Presence</div>

<div class="ph" role="img" aria-label="Photo of a man presenting on a whiteboard to colleagues" style="left:0;top:3124px;width:590px;height:436px;background:linear-gradient(135deg,#3fd6d0,#6a8fa8 50%,#8a7e74)"></div>
<div class="overlay-title" style="left:100px;top:3290px">We are Full Service<br>SEO Service</div>
<svg class="abs" style="left:1165px;top:3080px" width="35" height="130"><path d="M35 0C10 30 0 70 10 100C18 118 28 126 35 130Z" fill="#7a3fd4"/></svg>
<p class="eyebrow" style="left:639px;top:3144px">Why choose us</p>
<h2 class="abs" style="left:639px;top:3166px;font-size:32px;line-height:37px">Work With A Dedicated<br>SEO Agency</h2>
<div class="acc" style="top:3274px;height:100px">Keyword &amp; Market Research<span class="dot"></span><p style="margin-top:14px;font-size:11px;line-height:15px;color:var(--text)">At vero eos et accusamus et iusto odio dignissimos ducimus qui blanditiis praesentium voluptatum deleniti atque corrupti quos dolores et quas molestias excepturi</p></div>
<div class="acc" style="top:3391px;height:31px">Guest Post Outreach<span class="dot" style="top:5px"></span></div>
<div class="acc" style="top:3442px;height:31px">Landing Page Content<span class="dot" style="top:5px"></span></div>
<div class="acc" style="top:3494px;height:31px">Digital PR<span class="dot" style="top:5px"></span></div>

<p class="eyebrow" style="left:0;width:1200px;text-align:center;top:3673px">Featured projects</p>
<h2 class="abs" style="left:0;width:1200px;text-align:center;top:3692px;font-size:32px">Our Case Studies</h2>
<div class="case ph" role="img" aria-label="Office photo" style="left:0;width:95px;background:linear-gradient(135deg,#8a8a88,#d5d3cf)"></div>
<div class="case ph" role="img" aria-label="Photo of a laptop showing an SEO screen" style="left:117px;background:linear-gradient(135deg,#2d2f3a,#8a8f9c)"><b>SEO Marketing</b><small>View Here</small></div>
<div class="case ph" role="img" aria-label="Photo of a laptop showing analytics charts" style="left:446px;background:linear-gradient(135deg,#4a5058,#c9cdd2)"><b>SEO Analytics</b><small>View Here</small></div>
<div class="case ph" role="img" aria-label="Photo of two colleagues laughing at a laptop" style="left:775px;background:linear-gradient(135deg,#3b4658,#a59888)"><b>Keyword Ranking</b><small>View Here</small></div>
<div class="case ph" role="img" aria-label="Photo of a person working in an office" style="left:1104px;width:96px;background:linear-gradient(135deg,#d8c5a8,#eee8de)"><b>Optimi</b><small>View Here</small></div>
<div class="abs" style="left:536px;top:4040px;width:62px;height:7px;border-radius:4px;background:var(--accent)"></div>
<div class="abs" style="left:606px;top:4040px;width:12px;height:7px;border-radius:4px;background:var(--blue)"></div>
<div class="abs" style="left:626px;top:4040px;width:12px;height:7px;border-radius:4px;background:var(--blue)"></div>

<div class="abs" style="left:0;top:4080px;width:1200px;height:700px;background:linear-gradient(180deg,#ffffff,#f2f5fb 40%,#ffffff)"></div>
<p class="eyebrow" style="left:0;width:1200px;text-align:center;top:4135px">Blogs</p>
<h2 class="abs" style="left:0;width:1200px;text-align:center;top:4156px;font-size:32px">Read Our Latest News</h2>
<p class="para" style="left:290px;top:4203px;width:620px;text-align:center">Sed ut perspiciatis unde omnis iste natus error sit voluptatem accusantium doloremque laudantium, totam rem aperiam, eaque ipsa quae ab illo inventore veritatis et quasi architecto beatae vitae dicta sunt.</p>
<article class="post" style="left:115px"><div class="img" role="img" aria-label="Photo of hands reading a newspaper with a coffee cup" style="background:linear-gradient(135deg,#c9c2b8,#6f6a64)"></div><p class="date">March 21, 2020</p><h3>Sed ut perspiciatis unde omnis iste natus error sit</h3><p class="more">READ MORE</p></article>
<article class="post" style="left:444px"><div class="img" role="img" aria-label="Photo of a team working together at a desk" style="background:linear-gradient(135deg,#5c4a3e,#c7b9a8)"></div><p class="date">March 21, 2020</p><h3>Sed ut perspiciatis unde omnis iste natus error sit</h3><p class="more">READ MORE</p></article>
<article class="post" style="left:773px"><div class="img" role="img" aria-label="Photo of a laptop screen in blue light" style="background:linear-gradient(135deg,#1d5fd0,#9fc6f0 60%,#e6eef8)"></div><p class="date">March 21, 2020</p><h3>Sed ut perspiciatis unde omnis iste natus error sit</h3><p class="more">READ MORE</p></article>

<svg class="abs" style="left:0;top:4740px" width="1200" height="556" viewBox="0 0 1200 556">
  <defs>
    <linearGradient id="footGrad" x1="0" y1="0" x2="1" y2="1">
      <stop offset="0" stop-color="#1d66de"/>
      <stop offset="1" stop-color="#0a2fb8"/>
    </linearGradient>
  </defs>
  <path d="M0 110C150 20 320 40 520 90C760 150 980 60 1200 0V556H0Z" fill="#4a95f0" opacity=".45"/>
  <path d="M0 150C200 60 420 90 620 130C860 180 1020 120 1200 60V556H0Z" fill="url(#footGrad)"/>
</svg>
<div class="brand" style="left:0;width:1200px;text-align:center;top:4880px">RankHarbor</div>
<div class="abs" style="left:432px;top:4940px;width:1px;height:100px;background:rgba(255,255,255,.25)"></div>
<div class="abs" style="left:762px;top:4940px;width:1px;height:100px;background:rgba(255,255,255,.25)"></div>
<div class="fcol" style="left:121px">
  <svg width="22" height="30" viewBox="0 0 22 30"><path d="M11 0C4.9 0 0 4.9 0 11c0 8 11 19 11 19s11-11 11-19C22 4.9 17.1 0 11 0zm0 15a4 4 0 110-8 4 4 0 010 8z" fill="#8fd0ff"/></svg>
  <p>48 Harbour Lane, Suite 21</p><span>Our Address</span>
</div>
<div class="fcol" style="left:448px">
  <svg width="34" height="26" viewBox="0 0 34 26"><rect width="34" height="26" rx="3" fill="#8fd0ff"/><path d="M2 3l15 11L32 3" stroke="#0d3fc4" stroke-width="2.5" fill="none"/></svg>
  <p>hello@rankharbor.com</p><span>Mail</span>
</div>
<div class="fcol" style="left:767px">
  <svg width="28" height="28" viewBox="0 0 24 24"><path d="M6.6 10.8a15.1 15.1 0 006.6 6.6l2.2-2.2c.3-.3.7-.4 1-.2 1.1.4 2.3.6 3.6.6.6 0 1 .4 1 1V20c0 .6-.4 1-1 1C10.6 21 3 13.4 3 4c0-.6.4-1 1-1h3.5c.6 0 1 .4 1 1 0 1.3.2 2.5.6 3.6.1.3 0 .7-.2 1z" fill="#8fd0ff"/></svg>
  <p>020 5550 1847</p><span>Our Phone</span>
</div>
<nav class="fmenu"><span>Home</span><span>About us</span><span>Shop</span><span>Category ▾</span><span>Project</span><span>Blog</span><span>Contact</span></nav>
<div class="social" style="left:549px"></div>
<div class="social" style="left:587px"></div>
<div class="social" style="left:624px"></div>
<p class="abs" style="left:0;width:1200px;text-align:center;top:5243px;font-size:10px;color:#cfe0ff">Copyright © RankHarbor All Rights Reserve</p>

</body>
</html>
```